DORV2020 Save the date post card

Take the look and feel of the logo you designed and create a save the date postcard. 7L" by 5"H - print ready file with crop marks and bleeds.

Colors

Designer to choose colors to be used in the design.

Requirements
Must have
• The logo somewhere on the card.
• The following text:
• Save the Date
• June 1 - 4
• dorvsummit.ca
• Stronger United: Gather. Spark. Flourish.
Nice to have
• The following text:
• Vision: The vision of the DORV 2020 conference is to improve patient care by bringing together the Canadian Emergency Medicine community.
• Learning Objectives:
• By the end of the conference, delegates will be able to;
• • Apply up to date evidence to inform clinical decisions;
• • Acquire practical skills by participating in interactive sessions;
• • Connect and collaborate with other delegates;
• • Consider strategies to ensure career longevity; and
• • Influence the future direction of Emergency Medicine in Canada

```html
<!DOCTYPE html>
<html lang="en">
<head>
<meta charset="utf-8">
<title>DORV2020 Save the Date Postcard</title>
<link href="https://fonts.googleapis.com/css2?family=Bebas+Neue&family=Poppins:wght@400;500;600;700&family=Montserrat:wght@400;500;600&display=swap" rel="stylesheet">
<style>
  :root {
    --page-bg: #7a7a7a;
    --lavender: #c9d4f8;
    --lavender-light: #d6def9;
    --violet: #6a2fa6;
    --blue: #2d5bd8;
    --cyan: #13a6e6;
    --red: #e02424;
    --ink: #2b2b33;
    --muted: #4a4a55;
    --line: #b9b9be;
    --white: #ffffff;
  }
  * { box-sizing: border-box; margin: 0; padding: 0; }
  html, body { width: 1200px; height: 903px; overflow: hidden; }
  body { background: var(--page-bg); position: relative; font-family: "Poppins", sans-serif; }

  .card {
    position: absolute; width: 509px; height: 363px; overflow: hidden;
    box-shadow: 0 4px 12px rgba(0,0,0,.25);
  }

  /* Front */
  .card-front { left: 197px; top: 68px; background: var(--lavender); }
  .front-photo {
    position: absolute; left: 247px; top: 0; width: 262px; height: 363px;
    background: linear-gradient(90deg, #cfd6f5 0%, #bfc6e6 22%, #151517 30%, #2a2626 60%, #5b4c46 80%, #1b1a1a 100%);
  }
  .headline {
    position: absolute; left: 19px; top: 38px;
    font-family: "Bebas Neue", sans-serif; font-size: 46px; line-height: 1; letter-spacing: .5px;
    background: linear-gradient(90deg, var(--blue), var(--violet));
    -webkit-background-clip: text; background-clip: text; color: transparent;
  }
  .event-date {
    position: absolute; left: 20px; top: 86px;
    font-family: "Bebas Neue", sans-serif; font-size: 36px; line-height: 1; color: var(--red); letter-spacing: .5px;
  }
  .theme-tag {
    position: absolute; left: 21px; top: 132px; padding: 1px 5px;
    background: var(--cyan); color: var(--white); font-weight: 600; font-size: 13.5px; line-height: 18px;
  }
  .pillars { position: absolute; left: 21px; top: 160px; list-style: none; }
  .pillars li {
    display: flex; align-items: center; gap: 8px; height: 28px;
    font-size: 14px; color: var(--ink); font-weight: 500;
  }
  .pillars svg { width: 22px; height: 22px; }
  .brand {
    position: absolute; display: flex; align-items: center; gap: 6px;
    font-family: "Poppins", sans-serif; font-weight: 700; color: var(--violet);
  }
  .brand .dot { border-radius: 50%; background: var(--violet); }
  .brand-front { left: 22px; top: 292px; font-size: 18px; }
  .brand-front .dot { width: 12px; height: 12px; }
  .front-url {
    position: absolute; left: 21px; top: 330px; font-size: 13px; color: var(--ink);
  }

  /* Back */
  .card-back { left: 550px; top: 463px; background: var(--white); }
  .back-info {
    position: absolute; left: 0; top: 0; width: 271px; height: 363px;
    border-right: 2px solid var(--cyan); background: var(--white);
  }
  .back-photo {
    position: absolute; left: 0; top: 0; width: 269px; height: 148px;
    background: linear-gradient(180deg, #a8c8e6 0%, #8fa88a 45%, #4f6c3e 70%, #5d7f8f 100%);
  }
  .back-copy {
    position: absolute; left: 20px; top: 162px; width: 240px;
    font-family: "Montserrat", sans-serif; font-size: 8.4px; line-height: 1.25; color: var(--muted);
  }
  .back-copy .label { color: var(--violet); font-weight: 600; font-family: "Poppins", sans-serif; }
  .vision .label { font-size: 9.5px; margin-right: 8px; }
  .objectives-title { margin-top: 11px; font-size: 10.5px; }
  .objectives-intro { margin-top: 3px; }
  .objectives { list-style: none; margin-top: 5px; }
  .objectives li { display: flex; gap: 5px; margin-bottom: 4px; }
  .objectives svg { flex: none; width: 7px; height: 7px; margin-top: 2px; }
  .url-band {
    position: absolute; left: 0; bottom: 0; width: 269px; height: 34px;
    background: linear-gradient(90deg, #8a2a9c, var(--cyan));
    color: var(--white); font-family: "Montserrat", sans-serif; font-size: 12.5px;
    display: flex; align-items: center; justify-content: center;
  }
  .brand-back { left: 294px; top: 42px; font-size: 13px; }
  .brand-back .dot { width: 9px; height: 9px; }
  .stamp-box {
    position: absolute; left: 434px; top: 21px; width: 54px; height: 54px;
    border: 1px solid #9a9a9a;
  }
  .address-line { position: absolute; left: 299px; width: 189px; height: 1px; background: var(--line); }
  .back-photo-bw {
    position: absolute; left: 271px; top: 232px; width: 238px; height: 131px;
    background: linear-gradient(180deg, #ffffff 0%, #cfcfcf 35%, #6e6e6e 70%, #3a3a3a 100%);
  }
</style>
</head>
<body>

<section class="card card-front">
  <div class="front-photo" role="img" aria-label="Photo of a speaker presenting at a lectern with a microphone and laptop"></div>
  <h1 class="headline">SAVE THE DATE</h1>
  <p class="event-date">JUNE 1 - 4</p>
  <p class="theme-tag">Stronger United:</p>
  <ul class="pillars">
    <li>
      <svg viewBox="0 0 22 22"><circle cx="11" cy="11" r="10" fill="#fff" stroke="#6a7fe0" stroke-width="1"/><circle cx="11" cy="11" r="2.2" fill="#6a2fa6"/><circle cx="6" cy="7" r="1.5" fill="#2d5bd8"/><circle cx="16" cy="7" r="1.5" fill="#2d5bd8"/><circle cx="6" cy="15" r="1.5" fill="#2d5bd8"/><circle cx="16" cy="15" r="1.5" fill="#2d5bd8"/></svg>
      Gather
    </li>
    <li>
      <svg viewBox="0 0 22 22"><circle cx="11" cy="11" r="10" fill="#fff" stroke="#6a7fe0" stroke-width="1"/><circle cx="11" cy="9.5" r="3.5" fill="none" stroke="#6a2fa6" stroke-width="1.2"/><path d="M9.5 13.5h3v2.5h-3z" fill="#2d5bd8"/></svg>
      Spark
    </li>
    <li>
      <svg viewBox="0 0 22 22"><circle cx="11" cy="11" r="10" fill="#fff" stroke="#6a7fe0" stroke-width="1"/><circle cx="11" cy="11" r="5.5" fill="none" stroke="#6a2fa6" stroke-width="1.2"/><circle cx="11" cy="11" r="2" fill="#2d5bd8"/></svg>
      Flourish
    </li>
  </ul>
  <div class="brand brand-front"><span class="dot"></span>DORV2020</div>
  <p class="front-url">dorvsummit.ca</p>
</section>

<section class="card card-back">
  <div class="back-info">
    <div class="back-photo" role="img" aria-label="Photo of a city canal lined with trees and historic stone buildings"></div>
    <div class="back-copy">
      <p class="vision"><span class="label">Vision:</span>The vision of the DORV 2020 conference is to improve patient care by bringing together the Canadian Emergency Medicine community.</p>
      <p class="label objectives-title">Learning Objectives:</p>
      <p class="objectives-intro">By the end of the conference, delegates will be able to;</p>
      <ul class="objectives">
        <li><svg viewBox="0 0 8 8"><circle cx="4" cy="4" r="4" fill="#2d5bd8"/><path d="M2 4l1.4 1.4L6 2.8" stroke="#fff" stroke-width="1" fill="none"/></svg>Apply up to date evidence to inform clinical decisions;</li>
        <li><svg viewBox="0 0 8 8"><circle cx="4" cy="4" r="4" fill="#2d5bd8"/><path d="M2 4l1.4 1.4L6 2.8" stroke="#fff" stroke-width="1" fill="none"/></svg>Acquire practical skills by participating in interactive sessions;</li>
        <li><svg viewBox="0 0 8 8"><circle cx="4" cy="4" r="4" fill="#2d5bd8"/><path d="M2 4l1.4 1.4L6 2.8" stroke="#fff" stroke-width="1" fill="none"/></svg>Connect and collaborate with other delegates;</li>
        <li><svg viewBox="0 0 8 8"><circle cx="4" cy="4" r="4" fill="#2d5bd8"/><path d="M2 4l1.4 1.4L6 2.8" stroke="#fff" stroke-width="1" fill="none"/></svg>Consider strategies to ensure career longevity; and</li>
        <li><svg viewBox="0 0 8 8"><circle cx="4" cy="4" r="4" fill="#2d5bd8"/><path d="M2 4l1.4 1.4L6 2.8" stroke="#fff" stroke-width="1" fill="none"/></svg>Influence the future direction of Emergency Medicine in Canada</li>
      </ul>
    </div>
    <div class="url-band">www.dorvsummit.ca</div>
  </div>
  <div class="brand brand-back"><span class="dot"></span>DORV2020</div>
  <div class="stamp-box"></div>
  <div class="address-line" style="top:138px"></div>
  <div class="address-line" style="top:168px"></div>
  <div class="address-line" style="top:194px"></div>
  <div class="back-photo-bw" role="img" aria-label="Black and white photo of a conference panel seated at a table facing an audience"></div>
</section>

</body>
</html>
```